Creation of a construction/bricklaying business website

Following the template format of "Wendmoor 2", the following content would need to be included:
1. Landing page with 3 tiles that go to their own pages.
- Landing page to include background photo and description of services offered.
2. 3 tiles to include:
a) "Contact Us For A Free Quote or Friendly Discussion" Form (middle tile)
b) Case Studies and Testimonials
c) Certifications and Professional Membership
- Design logo to be used from previous PixelHarbor project. Example of logo attached below, please access full JPG files from our account.

Target Market(s)

Prospective clients seeking construction work (bricklaying speciality)

Industry/Entity Type

Residential Construction

Coding

Coded - Design and coding required

Number of Pages Required

4 page

Font styles to use
Sans Serif

Colors

Designer to choose colors to be used in the design.

Requirements
Must have
• Following the template format of "Wendmoor 2", the following content would need to be included:
• 1. Landing parent page with 3 tiles that go to the 3 child pages.
• - Landing page to include background photo and description of services offered.
• 2. 3 tiles to include:
• a) "Contact Us For A Free Quote or Friendly Discussion" Form (middle tile)
• b) Case Studies and Testimonials (first tile / left side)
• c) Certifications and Professional Memberships (third tile / right side) (This should include logos of the relevant organisations being displayed. Specifically QLT and the Keystone Pact QLT).
• - Design logo to be used from previous PixelHarbor project. Example of logo attached below, please access full JPG files from our account.
Nice to have
• Sleek and modern feel.
• Approachable in terms of how people can contact the company for a quote.
• Traditional pictures to give credibility and comfort around choosing this company.
Should not have
• Cheesy pictures
• Over-complicated
• Simple to use
• Easy URL domain name

```html
<!DOCTYPE html>
<html lang="en">
<head>
<meta charset="utf-8">
<title>R.T.Hale Construction Ltd</title>
<link href="https://fonts.googleapis.com/css2?family=Lato:wght@400;700&family=Open+Sans:wght@400;700&display=swap" rel="stylesheet">
<style>
:root{
  --brand:#1d4a9c;
  --brand-deep:#173f88;
  --ink:#2b2b2b;
  --muted:#555;
  --panel:#efefef;
  --line:#dcdcdc;
  --icon-bg:#e9ebf0;
  --white:#fff;
}
*{box-sizing:border-box;margin:0;padding:0}
html,body{width:816px;height:1200px;overflow:hidden;background:var(--white)}
body{position:relative;font-family:"Open Sans",sans-serif;color:var(--ink)}
.hero{position:absolute;left:0;top:0;width:816px;height:337px;
  background:linear-gradient(180deg,#3a4d6e 0%,#52617a 35%,#6b7584 65%,#3f4a58 100%)}
.brand{position:absolute;left:67px;top:14px;color:var(--white);font-family:"Lato",sans-serif;font-weight:700;line-height:1}
.brand .name{font-size:27px;letter-spacing:-.5px}
.brand .sub{font-size:9px;letter-spacing:1px;margin-top:3px}
.menu{position:absolute;left:735px;top:37px}
.hero-title{position:absolute;left:0;top:138px;width:816px;text-align:center;color:var(--white)}
.hero-title h1{font-family:"Open Sans",sans-serif;font-weight:700;font-size:56px;letter-spacing:-1px;line-height:1}
.hero-title p{font-family:"Lato",sans-serif;font-weight:700;font-size:15px;margin-top:13px}
.intro{position:absolute;left:0;top:337px;width:816px;height:91px;background:var(--brand);
  color:var(--white);font-family:"Lato",sans-serif;font-size:19px;line-height:27px;text-align:center;padding-top:18px}
.intro-arrow{position:absolute;left:392px;top:427px}
.services{position:absolute;left:47px;top:477px;width:722px;display:flex;justify-content:space-between;list-style:none}
.service{width:96px;text-align:center;font-family:"Lato",sans-serif;font-size:13px;color:var(--ink)}
.service .badge{width:54px;height:54px;border-radius:50%;background:var(--icon-bg);margin:0 auto 12px;display:flex;align-items:center;justify-content:center}
.about{position:absolute;left:140px;top:583px;width:536px;text-align:center;font-size:10px;line-height:23px;color:var(--ink)}
.cta{position:absolute;left:67px;top:685px;width:682px;height:75px;background:var(--panel);
  color:var(--brand);font-family:"Lato",sans-serif;font-size:15px;text-align:center;line-height:75px}
.tiles{position:absolute;left:67px;top:814px;width:682px;display:flex;gap:9px}
.tile{width:221px;height:293px;border:1px solid var(--line);position:relative;background:var(--white);overflow:hidden}
.tile .photo{height:120px}
.tile h2{font-family:"Lato",sans-serif;font-weight:400;font-size:14.6px;line-height:21px;color:var(--ink);margin:20px 8px 0 13px;white-space:nowrap;letter-spacing:-.1px}
.tile p{font-size:9.6px;line-height:17.6px;color:var(--muted);margin:9px 12px 0 13px;text-align:justify;letter-spacing:-.1px}
.tile .logos{display:flex;gap:10px;margin:6px 13px 0}
.tile .more{position:absolute;left:0;bottom:0;width:100%;height:30px;background:var(--panel);padding:9px 13px;
  font-size:9px;color:var(--brand);text-decoration:underline}
.photo-plan{background:linear-gradient(135deg,#f3c9a8,#e8b090 60%,#d9d0c8)}
.photo-team{background:linear-gradient(135deg,#8a8f98,#c9b9a6 50%,#5a5f66)}
.photo-award{background:linear-gradient(135deg,#d7dbe0,#9aa0a8 55%,#4a4e56)}
.footer{position:absolute;left:0;top:1161px;width:816px;height:39px;background:var(--brand-deep);
  color:var(--white);font-size:9.5px;text-align:center;line-height:39px}
</style>
</head>
<body>
<header class="hero" role="img" aria-label="Upward view of a modern glass office tower against a cloudy blue sky">
  <div class="brand"><div class="name">R.T.Hale</div><div class="sub">CONSTRUCTION LTD</div></div>
  <svg class="menu" width="14" height="13" viewBox="0 0 14 13" aria-label="Menu"><rect y="0" width="14" height="2.5" fill="#fff"/><rect y="5" width="14" height="2.5" fill="#fff"/><rect y="10" width="14" height="2.5" fill="#fff"/></svg>
  <div class="hero-title"><h1>R.T.Hale</h1><p>CONSTRUCTION LTD</p></div>
</header>

<section class="intro">R.T.Hale Construction Ltd is a construction company that has<br>expertise and experience in the following areas</section>
<svg class="intro-arrow" width="32" height="16" viewBox="0 0 32 16"><polygon points="0,0 32,0 16,16" fill="#1d4a9c"/></svg>

<ul class="services">
  <li class="service"><div class="badge"><svg width="24" height="26" viewBox="0 0 24 26"><rect x="3" y="1" width="16" height="22" fill="none" stroke="#1d4a9c" stroke-width="2"/><line x1="7" y1="7" x2="15" y2="7" stroke="#1d4a9c" stroke-width="2"/><line x1="7" y1="12" x2="15" y2="12" stroke="#1d4a9c" stroke-width="2"/><circle cx="18" cy="19" r="4" fill="#1d4a9c"/></svg></div>Extensions</li>
  <li class="service"><div class="badge"><svg width="22" height="26" viewBox="0 0 22 26"><rect x="3" y="6" width="7" height="19" fill="#1d4a9c"/><rect x="12" y="2" width="7" height="23" fill="#1d4a9c"/><line x1="0" y1="25" x2="22" y2="25" stroke="#1d4a9c" stroke-width="2"/></svg></div>New build</li>
  <li class="service"><div class="badge"><svg width="28" height="22" viewBox="0 0 28 22" fill="none" stroke="#1d4a9c" stroke-width="2"><rect x="1" y="1" width="26" height="20"/><line x1="1" y1="8" x2="27" y2="8"/><line x1="1" y1="15" x2="27" y2="15"/><line x1="10" y1="1" x2="10" y2="8"/><line x1="19" y1="1" x2="19" y2="8"/><line x1="14" y1="8" x2="14" y2="15"/><line x1="10" y1="15" x2="10" y2="21"/><line x1="19" y1="15" x2="19" y2="21"/></svg></div>Garden walls</li>
  <li class="service"><div class="badge"><svg width="28" height="22" viewBox="0 0 28 22"><rect x="1" y="3" width="18" height="16" fill="none" stroke="#1d4a9c" stroke-width="2"/><line x1="1" y1="11" x2="19" y2="11" stroke="#1d4a9c" stroke-width="2"/><line x1="20" y1="4" x2="27" y2="20" stroke="#1d4a9c" stroke-width="2"/></svg></div>Plastering</li>
  <li class="service"><div class="badge"><svg width="24" height="24" viewBox="0 0 24 24"><circle cx="8" cy="5" r="3" fill="#1d4a9c"/><rect x="5" y="9" width="5" height="7" fill="#1d4a9c"/><rect x="10" y="13" width="13" height="10" fill="#1d4a9c"/></svg></div>Brickwork</li>
  <li class="service"><div class="badge"><svg width="26" height="26" viewBox="0 0 26 26"><circle cx="9" cy="4" r="3" fill="#1d4a9c"/><rect x="6" y="8" width="6" height="10" fill="#1d4a9c"/><polygon points="12,25 25,25 20,15" fill="#1d4a9c"/></svg></div>Groundworks</li>
</ul>

<p class="about">We pride ourselves on attention to detail, pride in our completed project and client satisfaction. We believe in full transparency and this is reflected in the jobs we quote for you. We break down each step with both labour and materials cost so you can see exactly what you are paying for.</p>

<div class="cta">Feel free to get in touch and we can talk through what you are looking to achieve.</div>

<section class="tiles">
  <article class="tile">
    <div class="photo photo-plan" role="img" aria-label="Hands marking building plans with a red pen beside a yellow hard hat"></div>
    <h2>Case Studies and<br>Testimonials</h2>
    <p>Lorem ipsum dolor sit amet, consectetur ing elit, sed do eiusmod tempor incididunt ut labore et dolore magna aliqua.</p>
    <a class="more">Read More »</a>
  </article>
  <article class="tile">
    <div class="photo photo-team" role="img" aria-label="Two colleagues discussing a project at a workshop bench"></div>
    <h2>"Contact Us For A Free<br>Quote or Friendly Discussion"</h2>
    <p>Lorem ipsum dolor sit amet, consectetur ing elit, sed do eiusmod tempor incididunt ut labore et dolore magna aliqua.</p>
    <a class="more">Read More »</a>
  </article>
  <article class="tile">
    <div class="photo photo-award" role="img" aria-label="Business people shaking hands while presenting a certificate"></div>
    <h2 style="margin-top:14px">Certifications and<br>Professional Memberships</h2>
    <div class="logos">
      <svg width="58" height="22" viewBox="0 0 58 22" role="img" aria-label="Keystone Pact QLT membership badge"><rect width="58" height="22" fill="#1a2f5a"/></svg>
      <svg width="22" height="32" viewBox="0 0 22 32" role="img" aria-label="QLT membership badge"><rect width="22" height="32" fill="#9b1b30"/></svg>
    </div>
    <p>Lorem ipsum dolor sit amet, consectetur ing elit, sed do eiusmod tempor.</p>
    <a class="more">Read More »</a>
  </article>
</section>

<footer class="footer">Copyright © 2018 R.T.Hale Construction Ltd. All Rights Reserved. Privacy Policy | Terms Of Use</footer>
</body>
</html>
```